Family Ranch with a hobby vineyard needs 2 wine labels for our first harvest

Design 2 wine labels (front and back) with the Brindor Ranch logo.
Label 1:
Sauvignon Blanc
Alc. 12.5% by Vol.
Palos Verdes Peninsula - add as the region
Year 2022
Label 2:
Cabernet Sauvignon
Alc. 13.5% by Vol.
Year 2022
For the back label design:
GOVERNMENT WARNING: (1) According to the Surgeon General, women
should not drink alcoholic beverages during pregnancy because of the risk of
birth defects. (2) Consumption of alcoholic beverages impairs your ability to
drive a car or operate machinery, and may cause health problems.
Contains Sulfates.
750ML
I just received the bottles and have attached a picture.
Look and feel
Each slider illustrates characteristics of the customer's brand and the style your logo design should communicate.

```html
<!DOCTYPE html>
<html lang="en">
<head>
<meta charset="utf-8">
<title>Brindor Ranch – Wine Labels</title>
<link rel="stylesheet" href="https://fonts.googleapis.com/css2?family=Montserrat:wght@400;500;700&family=Roboto:wght@400;500&display=swap">
<style>
  :root {
    --navy: #23232f;
    --gold: #d3bb82;
    --green: #5b6a40;
    --red: #a3201f;
    --paper: #ffffff;
  }
  * { box-sizing: border-box; margin: 0; padding: 0; }
  html, body { width: 1200px; height: 627px; overflow: hidden; background: var(--paper); }
  .label-sheet {
    width: 1200px; height: 627px;
    display: flex; align-items: center; justify-content: center; gap: 38px;
  }
  .front-label {
    position: relative; width: 290px; height: 420px;
    font-family: "Montserrat", sans-serif; color: var(--gold); text-align: center;
  }
  .front-label svg { position: absolute; inset: 0; }
  .front-label.sauvignon { --accent: var(--green); }
  .front-label.cabernet { --accent: var(--red); }
  .brand-mark {
    position: absolute; left: 0; right: 0;
    display: flex; flex-direction: column; align-items: center;
  }
  .front-label .brand-mark { top: 70px; }
  .brand-dot { width: 64px; height: 64px; border-radius: 50%; border: 5px solid var(--gold); }
  .front-label .brand-dot { margin-bottom: 16px; }
  .brand-name {
    font-family: "Montserrat", sans-serif; font-weight: 500; color: var(--gold);
    letter-spacing: 0.04em; text-transform: uppercase; line-height: 1.1;
  }
  .front-label .brand-name { font-size: 26px; width: 160px; }
  .origin { position: absolute; top: 274px; left: 0; right: 0; font-size: 11.5px; line-height: 1.45; }
  .origin b { font-weight: 700; }
  .rule { position: absolute; top: 320px; left: 98px; width: 94px; height: 1px; background: var(--gold); opacity: .8; }
  .varietal { position: absolute; top: 334px; left: 0; right: 0; font-size: 15px; font-weight: 700; letter-spacing: .02em; }
  .abv { position: absolute; top: 358px; left: 0; right: 0; font-size: 11.5px; }

  .back-label {
    width: 224px; height: 397px; background: var(--navy);
    display: flex; flex-direction: column;
    font-family: "Roboto", sans-serif; color: var(--gold); text-align: center;
  }
  .back-label.sauvignon { --accent: var(--green); }
  .back-label.cabernet { --accent: var(--red); }
  .back-body { flex: 1; padding: 24px 16px 0; }
  .back-label .brand-mark { position: static; }
  .back-label .brand-dot { width: 40px; height: 40px; border-width: 3px; margin-bottom: 10px; }
  .back-label .brand-name { font-size: 19px; }
  .warning-title { margin-top: 22px; font-size: 10.5px; font-weight: 500; }
  .warning-text { margin-top: 11px; font-size: 10px; line-height: 1.3; }
  .back-band { height: 68px; background: var(--accent); }
</style>
</head>
<body>
<main class="label-sheet">

  <article class="front-label sauvignon">
    <svg viewBox="0 0 290 420" width="290" height="420">
      <defs>
        <clipPath id="inner-sb"><path d="M26 48 Q145 14 264 48 L278 48 L278 68 Q252 210 278 352 L278 372 L264 372 Q145 406 26 372 L12 372 L12 352 Q38 210 12 68 L12 48 Z"/></clipPath>
        <linearGradient id="map-sb" x1="0" y1="0" x2="1" y2="1"><stop offset="0" stop-color="#5b6a40"/><stop offset="1" stop-color="#4d5b36"/></linearGradient>
      </defs>
      <path fill="var(--green)" d="M14 38 Q145 0 276 38 L290 38 L290 60 Q262 210 290 360 L290 382 L276 382 Q145 420 14 382 L0 382 L0 360 Q28 210 0 60 L0 38 Z"/>
      <path fill="var(--navy)" d="M26 48 Q145 14 264 48 L278 48 L278 68 Q252 210 278 352 L278 372 L264 372 Q145 406 26 372 L12 372 L12 352 Q38 210 12 68 L12 48 Z"/>
      <g clip-path="url(#inner-sb)" role="img" aria-label="Map of the Palos Verdes Peninsula coastline with a star marking the ranch">
        <path fill="url(#map-sb)" d="M40 0 L300 0 L300 300 Q250 270 210 250 Q150 220 110 190 Q70 150 40 80 Z"/>
      </g>
      <path fill="none" stroke="var(--gold)" stroke-width="1.5" d="M36 58 Q145 26 254 58 L266 58 L266 76 Q242 210 266 344 L266 362 L254 362 Q145 394 36 362 L24 362 L24 344 Q48 210 24 76 L24 58 Z"/>
    </svg>
    <div class="brand-mark"><span class="brand-dot"></span><span class="brand-name">Brindor Ranch</span></div>
    <p class="origin">Palos Verdes Peninsula · <b>CA</b><br>Year 2022</p>
    <span class="rule"></span>
    <h2 class="varietal">SAUVIGNON BLANC</h2>
    <p class="abv">Alc. 12.5% by Vol</p>
  </article>

  <article class="back-label sauvignon">
    <div class="back-body">
      <div class="brand-mark"><span class="brand-dot"></span><span class="brand-name">Brindor Ranch</span></div>
      <p class="warning-title">GOVERNMENT WARNING:</p>
      <p class="warning-text">(1) According to the Surgeon General, women should not drink alcoholic beverages during pregnancy because of the risk of birth defects.</p>
      <p class="warning-text">(2) Consumption of alcoholic beverages impairs your ability to drive a car or operate machinery, and may cause health problems.</p>
      <p class="warning-text">Contains Sulfates.<br>750ML</p>
    </div>
    <div class="back-band"></div>
  </article>

  <article class="front-label cabernet">
    <svg viewBox="0 0 290 420" width="290" height="420">
      <defs>
        <clipPath id="inner-cs"><path d="M26 48 Q145 14 264 48 L278 48 L278 68 Q252 210 278 352 L278 372 L264 372 Q145 406 26 372 L12 372 L12 352 Q38 210 12 68 L12 48 Z"/></clipPath>
        <linearGradient id="map-cs" x1="0" y1="0" x2="1" y2="1"><stop offset="0" stop-color="#a3201f"/><stop offset="1" stop-color="#8e1b1b"/></linearGradient>
      </defs>
      <path fill="var(--red)" d="M14 38 Q145 0 276 38 L290 38 L290 60 Q262 210 290 360 L290 382 L276 382 Q145 420 14 382 L0 382 L0 360 Q28 210 0 60 L0 38 Z"/>
      <path fill="var(--navy)" d="M26 48 Q145 14 264 48 L278 48 L278 68 Q252 210 278 352 L278 372 L264 372 Q145 406 26 372 L12 372 L12 352 Q38 210 12 68 L12 48 Z"/>
      <g clip-path="url(#inner-cs)" role="img" aria-label="Map of the Palos Verdes Peninsula coastline with a star marking the ranch">
        <path fill="url(#map-cs)" d="M40 0 L300 0 L300 300 Q250 270 210 250 Q150 220 110 190 Q70 150 40 80 Z"/>
      </g>
      <path fill="none" stroke="var(--gold)" stroke-width="1.5" d="M36 58 Q145 26 254 58 L266 58 L266 76 Q242 210 266 344 L266 362 L254 362 Q145 394 36 362 L24 362 L24 344 Q48 210 24 76 L24 58 Z"/>
    </svg>
    <div class="brand-mark"><span class="brand-dot"></span><span class="brand-name">Brindor Ranch</span></div>
    <p class="origin">Palos Verdes Peninsula · <b>CA</b><br>Year 2022</p>
    <span class="rule"></span>
    <h2 class="varietal">CABERNET SAUVIGNON</h2>
    <p class="abv">Alc. 13.5% by Vol</p>
  </article>

  <article class="back-label cabernet">
    <div class="back-body">
      <div class="brand-mark"><span class="brand-dot"></span><span class="brand-name">Brindor Ranch</span></div>
      <p class="warning-title">GOVERNMENT WARNING:</p>
      <p class="warning-text">(1) According to the Surgeon General, women should not drink alcoholic beverages during pregnancy because of the risk of birth defects.</p>
      <p class="warning-text">(2) Consumption of alcoholic beverages impairs your ability to drive a car or operate machinery, and may cause health problems.</p>
      <p class="warning-text">Contains Sulfates.<br>750ML</p>
    </div>
    <div class="back-band"></div>
  </article>

</main>
</body>
</html>
```